DL Flyer announcing opening of Thistle Fern Row Homewares & Gift Store

To create 2 sided full colour DL Flyer which will be distributed by a letterbox drop to announce the opening of a delightful new homewares and gift store called "Thistle Fern Row Homewares" at 87 Marlowe Creek Road, Northbridge.

Thistle Fern Row Homewares offers a range of exclusive, bespoke, well-crafted decorative homewares and gifts. Our target market is well to do and aspirational, so we want the design of the flyer to match.

The owners, Brenda (a long-time resident of Northbridge) and Lorna have combined their love of homewares and years of retail experience to create this fresh and exciting new store.

Thistle Fern Row will cater for all those special occasions throughout the year but right now as we move into Christmas we have some beautiful Christmas decorations. Why not come in and visit Lorna who has 18 years experience in the Christmas industry and find out about our Christmas Tree decorating service.

Also we want a call to action so want to offer a 10% discount for people who bring the flyer in during the month of November

The store is open Tuesday to Friday 9.30am to 5.00pm and Saturday 10.00am to 4.00pm

Please find attached duck design we are using the coloured version (excluding the word 'duck' of course). The colour we have chosen for Thistle Fern Row is "Duck Egg Blue" and the font is Lucida Calligraphy.

Thank you

Target Market(s)

is well to do and aspirational

Industry/Entity Type

Store

• Lucida Calligraphy

Colors
cfeae6

Requirements
Must have
• the Duck. Discount voucher, address, look forward to being of service for many years to come. "Duck Egg Blue" colour tones

```html
<!DOCTYPE html>
<html lang="en">
<head>
<meta charset="utf-8">
<title>Thistle Fern Row Homewares – DL Flyer</title>
<link href="https://fonts.googleapis.com/css2?family=Oswald:wght@300;400&family=Rationale&family=Questrial&family=Open+Sans:ital,wght@1,700&family=Lato:wght@400&display=swap" rel="stylesheet">
<style>
  :root {
    --teal: #3a8f99;
    --duck-egg: #cfeae6;
    --navy: #1f2f5a;
    --ink: #1d1d1d;
    --white: #ffffff;
    --backdrop: #e9ecec;
    --photo-warm: #8a6a4c;
    --photo-light: #e6dccd;
  }
  * { margin: 0; padding: 0; box-sizing: border-box; }
  html, body { width: 1200px; height: 848px; overflow: hidden; background: var(--backdrop); }
  .canvas { position: relative; width: 1200px; height: 848px; }

  .flyer { position: absolute; top: 45px; width: 365px; height: 760px; overflow: hidden; }
  .flyer--front { left: 210px; background: var(--teal); }
  .flyer--back { left: 625px; background: var(--duck-egg); }

  .store-name {
    position: absolute; left: 0; width: 100%;
    text-align: center; color: var(--navy);
    font-family: "Rationale", sans-serif; font-weight: 400;
    font-size: 40px; line-height: 1.05; white-space: nowrap;
  }
  .store-name small { display: block; font-size: 22px; margin-top: 4px; }

  /* front */
  .shop-photo {
    position: absolute; left: 0; top: 0; width: 365px; height: 400px;
    background: linear-gradient(180deg, var(--photo-light) 0%, #b89c7c 45%, var(--photo-warm) 100%);
  }
  .hero-curve { position: absolute; left: 0; top: 300px; width: 365px; height: 110px; }
  .front-name { top: 95px; }
  .tagline {
    position: absolute; top: 250px; left: 0; width: 100%;
    text-align: center; color: var(--white);
    font-family: "Rationale", sans-serif; font-size: 20px; line-height: 24px;
    letter-spacing: 0.5px; text-shadow: 0 1px 3px rgba(0,0,0,0.45);
    white-space: nowrap;
  }
  .offer-title {
    position: absolute; top: 424px; left: 0; width: 100%; text-align: center;
    font-family: "Oswald", sans-serif; font-weight: 300; font-size: 52px;
    color: var(--duck-egg); letter-spacing: 1px; line-height: 60px;
    white-space: nowrap;
  }
  .rule { position: absolute; left: 53px; width: 260px; height: 2px; background: var(--duck-egg); }
  .rule--top { top: 491px; }
  .rule--bottom { top: 608px; }
  .discount {
    position: absolute; top: 496px; left: 0; width: 100%;
    display: flex; justify-content: center; align-items: flex-start; gap: 6px;
    color: var(--duck-egg); font-family: "Questrial", sans-serif;
  }
  .discount__number {
    font-family: "Oswald", sans-serif; font-weight: 400;
    font-size: 100px; line-height: 106px; letter-spacing: -2px;
  }
  .discount__side { display: flex; flex-direction: column; padding-top: 6px; }
  .discount__percent { font-size: 50px; line-height: 50px; }
  .discount__label { font-size: 20px; line-height: 22px; white-space: nowrap; }
  .discount-note {
    position: absolute; top: 615px; left: 0; width: 100%; text-align: center;
    font-family: "Rationale", sans-serif; font-size: 14px; color: var(--duck-egg);
    white-space: nowrap;
  }
  .hours { position: absolute; top: 645px; left: 0; width: 365px; height: 83px; background: var(--white); }
  .hours__title {
    position: absolute; top: 8px; width: 100%; text-align: center;
    font-family: "Open Sans", sans-serif; font-style: italic; font-weight: 700;
    font-size: 16px; color: var(--teal);
  }
  .hours__slot { position: absolute; top: 36px; text-align: center; font-family: "Lato", sans-serif; color: var(--ink); white-space: nowrap; }
  .hours__slot--week { left: 10px; width: 150px; }
  .hours__slot--sat { left: 215px; width: 140px; }
  .hours__day { font-size: 12px; letter-spacing: 0.3px; }
  .hours__time { font-size: 18px; margin-top: 1px; }
  .hours__amp {
    position: absolute; left: 162px; top: 30px; width: 50px; text-align: center;
    font-family: "Questrial", sans-serif; font-size: 46px; line-height: 1; color: var(--teal);
  }
  .address {
    position: absolute; bottom: 0; left: 0; width: 100%; height: 32px; line-height: 32px;
    text-align: center; color: var(--white); font-family: "Lato", sans-serif;
    font-size: 13px; letter-spacing: 0.5px; background: var(--teal); white-space: nowrap;
  }

  /* back */
  .band { position: absolute; left: 0; width: 100%; background: var(--teal); }
  .band--top { top: 0; height: 30px; }
  .band--bottom { bottom: 0; height: 32px; }
  .back-name { top: 100px; }
  .story {
    position: absolute; top: 247px; left: 0; width: 100%; text-align: center;
    font-family: "Rationale", sans-serif; font-size: 14.5px; line-height: 25.5px; color: var(--ink);
    white-space: nowrap;
  }
  .owner-photo {
    position: absolute; left: 18px; top: 532px; width: 130px; height: 196px;
    background: linear-gradient(180deg, var(--duck-egg) 0%, #d9b38a 40%, #f3efea 100%);
  }
  .tree-illustration {
    position: absolute; left: 148px; top: 535px; width: 212px; height: 193px;
    background: linear-gradient(180deg, var(--duck-egg) 0%, #a9c96a 55%, #c98a5a 100%);
    opacity: 0.85;
  }
</style>
</head>
<body>
<main class="canvas">

  <section class="flyer flyer--front" aria-label="Flyer front">
    <div class="shop-photo" role="img" aria-label="Photo of the store interior with shelves of homewares and warm lamps"></div>
    <svg class="hero-curve" viewBox="0 0 365 110" preserveAspectRatio="none" aria-hidden="true">
      <path d="M0 40 C 120 110, 260 95, 365 20 L365 110 L0 110 Z" fill="#cfeae6"/>
      <path d="M0 62 C 120 130, 260 115, 365 42 L365 110 L0 110 Z" fill="#3a8f99"/>
    </svg>
    <h1 class="store-name front-name">Thistle Fern Row<small>Homewares</small></h1>
    <p class="tagline">We offers a range of<br>exclusive, bespoke, well-crafted<br>decorative homewares<br>and gifts.</p>

    <h2 class="offer-title">OPENING SALE</h2>
    <div class="rule rule--top"></div>
    <div class="discount">
      <span class="discount__number">10</span>
      <span class="discount__side">
        <span class="discount__percent">%</span>
        <span class="discount__label">OFF ALL<br>PURCHASES</span>
      </span>
    </div>
    <div class="rule rule--bottom"></div>
    <p class="discount-note">Bring the flyer in during the month of November</p>

    <div class="hours">
      <p class="hours__title">Open Hours:</p>
      <div class="hours__slot hours__slot--week">
        <p class="hours__day">TUESDAY TO FRIDAY</p>
        <p class="hours__time">9.30am to 5pm</p>
      </div>
      <span class="hours__amp">&amp;</span>
      <div class="hours__slot hours__slot--sat">
        <p class="hours__day">SATURDAY</p>
        <p class="hours__time">10am to 4pm</p>
      </div>
    </div>
    <p class="address">87 MARLOWE CREEK ROAD, NORTHBRIDGE</p>
  </section>

  <section class="flyer flyer--back" aria-label="Flyer back">
    <div class="band band--top"></div>
    <h1 class="store-name back-name">Thistle Fern Row<small>Homewares</small></h1>
    <p class="story">
      The owners, Brenda (a long-time resident of Northbridge)<br>
      and Lorna have combined their love of homewares and<br>
      years of retail experience to create this<br>
      fresh and exciting new store.<br>
      Thistle Fern Row Homewares will cater for all those<br>
      special occasions throughout the year but<br>
      right now as we move into Christmas we have some<br>
      beautiful Christmas decorations.<br>
      Why not come in and visit Lorna who has 18 years<br>
      experience in the Christmas industry and find out about<br>
      our Christmas Tree decorating service.
    </p>
    <div class="owner-photo" role="img" aria-label="Portrait photo of the store owner"></div>
    <div class="tree-illustration" role="img" aria-label="Illustration of decorated Christmas trees and wrapped gifts"></div>
    <div class="band band--bottom"></div>
  </section>

</main>
</body>
</html>
```